Cybersecurity company is looking for business card.

I need a business card design for our company, we are a cybersecurity company providing advance technology to protect agains any kind of malware. We need a fresh modern design it should communicate modern, technology and growth.

Target Market(s)

Business to business

Industry/Entity Type

Business

Contact Information for Business Card

Should have location, address, fax, mobile, phone, email and website.

Requirements
Must have
• Must follow company's logo color and style. Must have the company's log on its.

```html
<!DOCTYPE html>
<html lang="en">
<head>
<meta charset="utf-8">
<title>Nuvrakel business card</title>
<link href="https://fonts.googleapis.com/css2?family=Roboto:wght@300;400;700&display=swap" rel="stylesheet">
<style>
  :root {
    --ink: #0b0b0b;
    --paper: #f4f4f4;
    --paper-shade: #e2e2e2;
    --accent: #c8202e;
    --stage: #d8d5cf;
    --light-text: #e9e9e9;
    --muted: #3a3a3a;
  }
  * { margin: 0; padding: 0; box-sizing: border-box; }
  html, body { width: 1200px; height: 892px; overflow: hidden; }
  body {
    background: var(--stage);
    font-family: "Roboto", Arial, sans-serif;
    position: relative;
  }
  .card {
    position: absolute;
    width: 560px;
    height: 320px;
    overflow: hidden;
    box-shadow: 0 6px 18px rgba(0,0,0,.25);
    background: linear-gradient(135deg, var(--paper), var(--paper-shade));
  }
  .card-front { left: 320px; top: 70px; }
  .card-back { left: 320px; top: 470px; }

  .wordmark {
    font-weight: 700;
    color: var(--ink);
    letter-spacing: 1px;
    line-height: 1;
    display: flex;
    align-items: center;
    gap: 10px;
    white-space: nowrap;
  }
  .wordmark .mark-square { width: 12px; height: 12px; background: var(--accent); flex: none; }

  /* front */
  .front-white { position: absolute; left: 0; top: 0; width: 100%; height: 168px; }
  .front-white .wordmark { position: absolute; right: 50px; top: 54px; font-size: 58px; }
  .location {
    position: absolute; left: 30px; bottom: 16px;
    font-size: 15px; font-weight: 300; color: var(--muted);
    display: flex; align-items: center; gap: 8px;
  }
  .front-band {
    position: absolute; left: 0; top: 168px; width: 100%; height: 152px;
    background: var(--ink);
  }
  .stripes { position: absolute; left: 0; top: 6px; width: 100%; height: 12px; }
  .stripes::before, .stripes::after {
    content: ""; position: absolute; left: 0; width: 100%; height: 2px; background: var(--accent);
  }
  .stripes::before { top: 0; }
  .stripes::after { top: 7px; }
  .contact-main {
    position: absolute; left: 30px; bottom: 24px;
    color: var(--light-text); font-size: 14px; font-weight: 300; line-height: 1.55;
  }
  .contact-phones {
    position: absolute; right: 30px; top: 34px;
    color: var(--light-text); font-size: 13px; font-weight: 300; line-height: 1.6; text-align: right;
  }
  .phone-icons { display: flex; gap: 5px; justify-content: flex-end; margin-bottom: 6px; }
  .phone-icons svg { width: 16px; height: 16px; display: block; }

  /* back */
  .back-band {
    position: absolute; top: 0; left: 160px; width: 240px; height: 100%;
    background: var(--ink);
    display: flex; align-items: center; justify-content: center;
  }
  .vstripes { position: absolute; top: 0; width: 9px; height: 100%; }
  .vstripes::before, .vstripes::after {
    content: ""; position: absolute; top: 0; width: 2px; height: 100%; background: var(--accent);
  }
  .vstripes::before { left: 0; }
  .vstripes::after { left: 7px; }
  .vstripes.left { left: 10px; }
  .vstripes.right { right: 10px; }
  .back-band .wordmark { color: #ffffff; font-size: 44px; }
</style>
</head>
<body>

<section class="card card-front" aria-label="Business card front">
  <div class="front-white">
    <div class="wordmark"><span class="mark-square"></span>nuvrakel</div>
    <p class="location">
      <svg width="12" height="16" viewBox="0 0 12 16" aria-hidden="true">
        <path d="M6 0a6 6 0 0 0-6 6c0 4.5 6 10 6 10s6-5.5 6-10a6 6 0 0 0-6-6z" fill="#c8202e"/>
        <circle cx="6" cy="6" r="2.2" fill="#f4f4f4"/>
      </svg>
      Corvessa - Eastland
    </p>
  </div>
  <div class="front-band">
    <div class="stripes"></div>
    <div class="contact-phones">
      <div class="phone-icons" aria-hidden="true">
        <svg viewBox="0 0 16 16"><rect width="16" height="16" rx="2" fill="#c8202e"/><path d="M4 6c0-1.5 8-1.5 8 0v1h-2V6H6v1H4z M5 8h6l1 4H4z" fill="#fff"/></svg>
        <svg viewBox="0 0 16 16"><rect width="16" height="16" rx="2" fill="#c8202e"/><rect x="4" y="3" width="8" height="4" fill="#fff"/><rect x="3" y="7" width="10" height="6" rx="1" fill="#fff"/></svg>
        <svg viewBox="0 0 16 16"><rect width="16" height="16" rx="2" fill="#c8202e"/><rect x="5" y="2.5" width="6" height="11" rx="1" fill="none" stroke="#fff" stroke-width="1.4"/></svg>
      </div>
      <p>04 555 0100</p>
      <p>04 555 0101</p>
      <p>+44 52 555 0102</p>
    </div>
    <div class="contact-main">
      <p>www.nuvrakel.com</p>
      <p>name.surname@nuvrakel.com</p>
      <p>Harbor Tech Park (HTP) - Coastal Avenue</p>
    </div>
  </div>
</section>

<section class="card card-back" aria-label="Business card back">
  <div class="back-band">
    <div class="vstripes left"></div>
    <div class="wordmark"><span class="mark-square"></span>nuvrakel</div>
    <div class="vstripes right"></div>
  </div>
</section>

</body>
</html>
```